Up and Coming Granola Brand Needs Labels and Logo Design

We need a label design for a new Granola Company called Fennly's Granola. We create delicious hand-crafted granolas that are not only tasty, but good for you!

We would also like a 'modern' logo, similar to the attached one.
The logo name is "Fennly's". The concept would be to have the word "Fennly's" in the banner, and "Granola" below in font. Eventually the product line will expand to include other items, and we would like a logo that allows us to match the product to the logo name.

The logo should integrate well with the packaging label.

We plan on using light brown resealable packaging for our granola, and would prefer earthy colours, or colours that would complement the packaging for the labels. We intend to print the designs on labels, and paste them on the front and back of the package. (Package dimensions and image of package are included in attachments)

We plan on having a few flavours of Granola, and that would have some small changes on the label design.

Some of our ingredients in our granola would include Oats, Dried fruit, nuts and various grains.

It would be good if the labels could feature oats (perhaps an ear of oats, or something to similar effect)
Updates

have added dimensions to the packaging to give a sense of size for reference. image of the packaging we will be using also added! Added Wednesday, May 11, 2016

Reason: Loving the submissions so far! Can't wait to see what else you can come up with! Have extended the deadline to give some breathing room and time for tweaking!

Target Market(s)

20s-40s

Industry/Entity Type

Food Store

Logo Text

Fennly's

Font styles to use
Serif
Decorative

Requirements
Must have
• -Colours that complement the packaging colour (light brown)
• -Can be printed on white labels that will be stuck on the packaging (both for the front of packaging; that has a window, and the back of the packaging; no window)
• -simple and stylish design that entices buyers to purchase the product
• -A flexible logo that can transition seamlessly between different product lines
• - Sections for "our story", "nutritional information", "ingredients, etc on the back label.
Nice to have
• -as attached in image samples for the brief.
• - other trendy designs that are currently popular
• - different colour schemes for different flavours. Currently there are 3 flavours; 1) Mocha Almond, 2) Matcha with White Chocolate and Cashews, and 3) Classic Fruit and Nut.
Should not have
• -colours that stand out too much, or do not fit the design brief
• -overly complicated designs that take away from the main theme of awesome granola

```html
<!DOCTYPE html>
<html lang="en">
<head>
<meta charset="UTF-8">
<title>Fennly's Granola – Crunchy Fruit &amp; Oat Front Label</title>
<link href="https://fonts.googleapis.com/css2?family=Open+Sans:wght@400;600;700&display=swap" rel="stylesheet">
<style>
  :root {
    --backdrop: #f4f2ee;
    --label: #ffffff;
    --label-edge: #e4e0d8;
    --brand-ink: #3b3a22;
    --flavour-red: #c1272d;
    --copy-red: #b8322f;
  }
  html, body {
    margin: 0;
    width: 1200px;
    height: 1000px;
    overflow: hidden;
    background: var(--backdrop);
  }
  .canvas {
    width: 1200px;
    height: 1000px;
    display: flex;
    align-items: center;
    justify-content: center;
  }
  .front-label {
    box-sizing: border-box;
    width: 600px;
    height: 790px;
    background: var(--label);
    border: 1px solid var(--label-edge);
    display: flex;
    flex-direction: column;
    align-items: center;
    font-family: "Open Sans", Arial, sans-serif;
    padding-top: 118px;
  }
  .brand {
    display: flex;
    flex-direction: column;
    align-items: center;
    color: var(--brand-ink);
    font-weight: 700;
    line-height: 1;
  }
  .brand-name {
    font-size: 50px;
  }
  .brand-line {
    font-size: 20px;
    letter-spacing: 1.5px;
    margin-top: 6px;
  }
  .flavour {
    margin-top: 128px;
    text-align: center;
    color: var(--flavour-red);
    font-weight: 700;
    line-height: 1;
  }
  .flavour-title {
    font-size: 112px;
    letter-spacing: -1px;
  }
  .flavour-sub {
    font-size: 54px;
    font-weight: 600;
    margin-top: 10px;
  }
  .blurb {
    margin-top: auto;
    margin-bottom: 44px;
    width: 480px;
    text-align: center;
    font-size: 14px;
    line-height: 1.55;
    color: var(--copy-red);
  }
</style>
</head>
<body>
  <main class="canvas">
    <section class="front-label">
      <div class="brand">
        <span class="brand-name">Fennly's</span>
        <span class="brand-line">GRANOLA</span>
      </div>
      <div class="flavour">
        <div class="flavour-title">CRUNCHY</div>
        <div class="flavour-sub">Fruit &amp; Oat</div>
      </div>
      <p class="blurb">Hand-crafted granola baked in small batches with whole oats, dried fruit and toasted nuts. A crunchy, wholesome bite for breakfast or any time of day.</p>
    </section>
  </main>
</body>
</html>
```